Business card for our start up Automotive Shop

Clean business card design for our new automotive shop Brightline Motor Works. This card will be the template for all of our staff member including technicians and service advisors.

Brightline Motor Works is an automotive service shop catering to US domestic and asian import vehicles. We are a service and maintenance full service facility. Our aim is to provide the best quality workmanship and the best customer service experience in our industry.

Our target market are young professionals to people with families. We are not targeting a younger audience or the car modification scene. The card should be appealing to women of the 30+ age demographic.

We are a shop of younger professionals instead of an older crowd. The card design should reflect as such.

Target Market(s)

30+ Female demographic and 30+ male.

Industry/Entity Type

Automotive

Contact Information for Business Card

Must be clean and appealing to clients. Large enough and easy to read print.

Font styles to use
Sans Serif

Colors
f78f20
ffffff
b2b2b2
dddddd

Requirements
Must have
• Address, website and phone number
• 42-15 58th Ave
• Cedar Hollow NY 11462
• (718) 402-3917
• brightlinemotorworks.com
• There must be an area to add a Name and e-mail address for personalization purposes.
Nice to have
• Back of the card should have website.
• I would also like to incorporate yelp, google+, Facebook, and instagram widgets. Will add the exact pages but everything can be @ or / brightlinemotorworks
• That can be added on the back of the card.

```html
<!DOCTYPE html>
<html lang="en">
<head>
<meta charset="utf-8">
<title>Brightline Motor Works — Business Card</title>
<link rel="stylesheet" href="https://fonts.googleapis.com/css2?family=Montserrat:wght@500;700;800&display=swap">
<style>
  :root {
    --orange: #f78f20;
    --orange-deep: #ef6f2e;
    --orange-light: #f9b23a;
    --white: #ffffff;
    --grey: #b2b2b2;
    --grey-light: #dddddd;
    --backdrop: #c8c8ca;
  }
  * { box-sizing: border-box; margin: 0; padding: 0; }
  html, body {
    width: 1200px; height: 900px; overflow: hidden;
    background: var(--backdrop);
    font-family: "Montserrat", Arial, sans-serif;
  }
  .stage {
    position: relative; width: 1200px; height: 900px;
    display: flex; flex-direction: column; align-items: center; justify-content: center; gap: 36px;
  }
  .card {
    position: relative; width: 700px; height: 400px; overflow: hidden;
    box-shadow: 0 10px 28px rgba(0,0,0,.22);
  }
  .card-front {
    background: radial-gradient(ellipse at 62% 30%, var(--orange-light) 0%, var(--orange) 45%, var(--orange-deep) 100%);
    display: flex; align-items: center; justify-content: center;
  }
  .wordmark {
    display: flex; align-items: center; gap: 18px;
    font-weight: 800; text-transform: uppercase; letter-spacing: 1px; line-height: 1.05;
  }
  .wordmark-dot { width: 64px; height: 64px; border-radius: 50%; flex: none; }
  .card-front .wordmark { color: var(--white); font-size: 40px; }
  .card-front .wordmark-dot { background: var(--white); }

  .card-back { display: flex; background: var(--white); }
  .back-brand {
    position: relative; width: 47%; height: 100%;
    display: flex; align-items: center; justify-content: center;
    border-left: 14px solid var(--orange);
  }
  .back-brand .wordmark { color: var(--orange); font-size: 24px; gap: 12px; }
  .back-brand .wordmark-dot { width: 40px; height: 40px; background: var(--orange); }
  .back-details {
    position: relative; flex: 1; height: 100%; color: var(--white);
    background: radial-gradient(ellipse at 30% 10%, var(--orange-light) 0%, var(--orange) 45%, var(--orange-deep) 100%);
    padding: 58px 40px 0 40px;
  }
  .person-name { font-size: 40px; font-weight: 800; line-height: 1; }
  .person-role { font-size: 12px; font-weight: 500; letter-spacing: 1px; margin: 6px 0 0 34px; text-transform: uppercase; }
  .contact-list { list-style: none; margin-top: 42px; font-size: 17px; font-weight: 500; line-height: 1.3; }
  .contact-list li { display: flex; gap: 12px; align-items: flex-start; margin-bottom: 10px; }
  .contact-list svg { flex: none; width: 16px; height: 16px; margin-top: 3px; }
  .social-row { position: absolute; right: 30px; bottom: 26px; display: flex; gap: 10px; }
  .social-spot { width: 26px; height: 26px; border-radius: 50%; background: var(--white); }
</style>
</head>
<body>
<main class="stage">
  <section class="card card-front">
    <div class="wordmark"><span class="wordmark-dot"></span><span>Brightline<br>Motor Works</span></div>
  </section>

  <section class="card card-back">
    <div class="back-brand">
      <div class="wordmark"><span class="wordmark-dot"></span><span>Brightline<br>Motor Works</span></div>
    </div>
    <div class="back-details">
      <h1 class="person-name">YOUR NAME</h1>
      <p class="person-role">Designation</p>
      <ul class="contact-list">
        <li>
          <svg viewBox="0 0 16 16" aria-hidden="true"><path d="M8 1a5 5 0 0 0-5 5c0 4 5 9 5 9s5-5 5-9a5 5 0 0 0-5-5z" fill="none" stroke="#fff" stroke-width="1.6"/><circle cx="8" cy="6" r="1.8" fill="#fff"/></svg>
          <span>42-15 58th Ave<br>Cedar Hollow NY 11462</span>
        </li>
        <li>
          <svg viewBox="0 0 16 16" aria-hidden="true"><circle cx="8" cy="8" r="7.5" fill="#fff"/><path d="M5.5 4.5l1.3 1.5-.8 1a5 5 0 0 0 2.6 2.6l1-.8 1.5 1.3-.9 1.2c-2.8-.4-5.2-2.8-5.6-5.6z" fill="#f78f20"/></svg>
          <span>(718) 402-3917</span>
        </li>
        <li>
          <svg viewBox="0 0 16 16" aria-hidden="true"><rect x="1" y="3.5" width="14" height="9.5" fill="none" stroke="#fff" stroke-width="1.4"/><path d="M1 3.5l7 5.5 7-5.5" fill="none" stroke="#fff" stroke-width="1.4"/></svg>
          <span>brightlinemotorworks.com</span>
        </li>
      </ul>
      <div class="social-row" aria-label="Social media links">
        <span class="social-spot"></span><span class="social-spot"></span><span class="social-spot"></span>
      </div>
    </div>
  </section>
</main>
</body>
</html>
```